We are in search of a new business card design for our business. We have a Mexican Grocery Store called Tortilla Grove Market, we would like to see that some have mexican design, but we are open to any type of designs.

Phone: to be announced
Fax: to be announced

Address is:
2415 Calloway Blvd
Elmridge, MD 21340

```html
<!DOCTYPE html>
<html lang="en">
<head>
<meta charset="utf-8">
<title>Tortilla Grove Market – Business Card</title>
<link href="https://fonts.googleapis.com/css2?family=Open+Sans:wght@400;600&display=swap" rel="stylesheet">
<style>
  :root {
    --backdrop: #3a3b3d;
    --card-white: #ffffff;
    --green-deep: #1e7e3e;
    --green-bright: #2db34a;
    --brand-red: #b2162a;
    --name-red: #a3182b;
    --text-dark: #3c3c3c;
    --divider: #9a9a9a;
  }
  html, body {
    margin: 0;
    padding: 0;
    width: 1200px;
    height: 977px;
    overflow: hidden;
    background: var(--backdrop);
    font-family: "Open Sans", Arial, sans-serif;
  }
  .business-card {
    position: absolute;
    left: 180px;
    top: 248px;
    width: 840px;
    height: 480px;
    background: var(--card-white);
    overflow: hidden;
    box-shadow: 0 10px 30px rgba(0,0,0,0.35);
  }
  .card-sweep {
    position: absolute;
    inset: 0;
    width: 840px;
    height: 480px;
  }
  .brand-lockup {
    position: absolute;
    left: 0;
    width: 840px;
    top: 98px;
    display: flex;
    justify-content: center;
    align-items: center;
    gap: 12px;
  }
  .brand-dot {
    width: 22px;
    height: 22px;
    border-radius: 50%;
    background: var(--brand-red);
  }
  .brand-name {
    font-size: 30px;
    font-weight: 600;
    color: var(--brand-red);
    letter-spacing: 0.5px;
  }
  .contact-person {
    position: absolute;
    right: 440px;
    top: 262px;
    text-align: right;
  }
  .person-name {
    font-size: 25px;
    color: var(--name-red);
    letter-spacing: 0.5px;
    line-height: 1.1;
  }
  .person-role {
    font-size: 15px;
    font-weight: 600;
    color: var(--text-dark);
  }
  .contact-divider {
    position: absolute;
    left: 420px;
    top: 232px;
    width: 1.5px;
    height: 100px;
    background: linear-gradient(to bottom, rgba(154,154,154,0), var(--divider) 30%, var(--divider) 70%, rgba(154,154,154,0));
  }
  .contact-details {
    position: absolute;
    left: 446px;
    top: 236px;
    font-size: 15px;
    line-height: 1.45;
    color: var(--text-dark);
  }
  .contact-details p { margin: 0; }
</style>
</head>
<body>
  <div class="business-card">
    <svg class="card-sweep" viewBox="0 0 840 480" aria-hidden="true">
      <path d="M0,392 C260,420 660,390 840,168 L840,480 L0,480 Z" fill="var(--green-bright)"/>
      <path d="M0,400 C270,428 670,400 840,190 L840,480 L0,480 Z" fill="var(--card-white)"/>
      <path d="M0,404 C270,432 680,405 840,205 L840,480 L0,480 Z" fill="var(--green-deep)"/>
      <path d="M0,392 C260,420 660,390 840,168 L840,175 C668,394 262,424 0,396 Z" fill="var(--green-bright)"/>
    </svg>

    <div class="brand-lockup">
      <span class="brand-dot"></span>
      <span class="brand-name">Tortilla Grove Market</span>
    </div>

    <div class="contact-person">
      <div class="person-name">DANIEL REYES</div>
      <div class="person-role">Manager</div>
    </div>

    <div class="contact-divider"></div>

    <div class="contact-details">
      <p>2415 Calloway Blvd</p>
      <p>Elmridge, MD 21340</p>
      <p>Phone: 01 47 26 38 51</p>
    </div>
  </div>
</body>
</html>
```